Design profile for MuroDeck Nordhaven

I had a logo competition here recently, and was left with two logos that I could not choose between. Therefore, I create this competition where I want a complete design package or a visual identity for the company. I want you to create design elements that can be used both in print and online. (letterhead, envelopes, business card, website, facebook, etc.) I have also attached a picture of the car I have ordered. I'm happy if you can show how the design can be used on that as well.
What is important is that the logos are treated individually, and that the design you create reflects or builds up under the logo. I want the design to be recognizable and to have a connection with the logo and what we do. (take fizzo lumo as an example. if you remove the name, but keep the red color and the white line, then you will recognize which brand it is about right away)
You choose whether you want to make proposals only for one logo, or or both, but it is important that they are treated individually. The best overall package determines which logo I use.
I have also added an image that you can use as an example background if you want it in a facebook banner for example.
It is important that the design looks professional and unique. A number of designs have come in, but many of the designs are very similar and general. Here is a video of the printer if you need inspiration: https://clipvault.example/v/Q8ZtrMx2LwK

Industry/Entity Type

WallPrinting

Requirements
Must have
• Unique an professional design that can be used both online and print
Nice to have
• Show how to use the design on a VX Tully. (see photos attached)
Should not have
• The design can be simple, but not too simple and general. I want it to give the company an identity

```html
<!DOCTYPE html>
<html lang="en">
<head>
<meta charset="utf-8">
<title>MuroDeck Nordhaven – Stationery Set</title>
<link rel="stylesheet" href="https://fonts.googleapis.com/css2?family=Arimo:wght@400;700&display=swap">
<style>
  :root {
    --bg: #c9c9cb;
    --paper: #f7f7f7;
    --ink: #2a2a2a;
    --dark: #2e2e2e;
    --muted: #6b6b6b;
    --rule: #9a9a9a;
    --pink: #ef7fb0;
    --yellow: #f3c10d;
    --magenta: #d0257f;
    --purple: #5a2a8a;
    --navy: #1f2a6b;
    --cyan: #2ab1e8;
    --maroon: #6e1634;
  }
  * { margin: 0; padding: 0; box-sizing: border-box; }
  html, body { width: 1200px; height: 800px; overflow: hidden; }
  body {
    background: var(--bg);
    font-family: "Arimo", Arial, sans-serif;
    color: var(--ink);
    position: relative;
  }
  .sheet { position: absolute; box-shadow: 0 6px 18px rgba(0,0,0,.18); overflow: hidden; }
  .sheet--light { background: var(--paper); }
  .sheet--dark { background: var(--dark); color: #f2f2f2; }

  .brand {
    display: flex; align-items: center; gap: 6px;
    font-weight: 700; white-space: nowrap; position: absolute;
  }
  .brand__mark { width: 9px; height: 9px; background: currentColor; flex: none; }

  .address {
    position: absolute; font-size: 7px; line-height: 1.35; color: var(--muted);
  }
  .address--ruled-right { text-align: right; padding-right: 6px; border-right: 1px solid var(--rule); }
  .address--ruled-left { padding-left: 6px; border-left: 1px solid var(--rule); }

  .color-band { position: absolute; }
  .color-band--vertical {
    background: linear-gradient(180deg, var(--pink) 0%, var(--yellow) 22%, var(--magenta) 42%, var(--purple) 58%, var(--cyan) 74%, var(--navy) 88%, var(--maroon) 100%);
  }
  .color-band--folder {
    background: linear-gradient(180deg, var(--purple) 0%, var(--maroon) 30%, var(--navy) 55%, var(--magenta) 72%, #e9782c 84%, var(--cyan) 93%, var(--pink) 100%);
  }

  /* Letterhead */
  .letterhead { left: 60px; top: 190px; width: 300px; height: 424px; }
  .letterhead .brand { left: 28px; top: 40px; font-size: 13px; }
  .letterhead .address { right: 26px; top: 36px; }
  .letterhead .color-band { right: 0; bottom: 0; width: 22px; height: 120px; }

  /* Folder */
  .folder { left: 400px; top: 170px; width: 320px; height: 452px; }
  .folder .brand { left: 40px; top: 70px; font-size: 22px; gap: 9px; }
  .folder .brand__mark { width: 14px; height: 14px; }
  .folder .color-band { left: 0; bottom: 0; width: 60px; height: 190px; }

  /* Envelope front */
  .envelope-front { left: 770px; top: 120px; width: 360px; height: 180px; }
  .envelope-front .brand { left: 26px; top: 34px; font-size: 12px; }
  .envelope-front .address { left: 26px; bottom: 24px; }
  .envelope-front .color-band { right: 0; top: 0; width: 18px; height: 180px; }

  /* Envelope back */
  .envelope-back { left: 770px; top: 330px; width: 360px; height: 180px; }
  .envelope-back .flap { position: absolute; left: 0; top: 0; width: 100%; height: 100%; }
  .envelope-back .web { position: absolute; left: 0; right: 0; top: 22px; text-align: center; font-size: 7px; letter-spacing: .08em; color: #d8d8d8; }
  .envelope-back .color-band { right: 0; top: 0; width: 18px; height: 180px; }

  /* Business cards */
  .card { width: 170px; height: 100px; top: 575px; }
  .card--light { left: 770px; }
  .card--light .brand { right: 14px; top: 16px; font-size: 10px; gap: 4px; }
  .card--light .brand__mark { width: 7px; height: 7px; }
  .card--light .address { right: 14px; top: 36px; font-size: 6px; text-align: right; }
  .card--light .person { position: absolute; left: 14px; bottom: 14px; padding-left: 5px; border-left: 1px solid var(--rule); }
  .person__name { font-size: 8px; font-weight: 700; }
  .person__role { font-size: 6px; color: var(--muted); }
  .card--dark { left: 960px; }
  .card--dark .brand { left: 22px; top: 42px; font-size: 11px; gap: 5px; }
  .card--dark .brand__mark { width: 7px; height: 7px; }
  .card--dark .color-band { right: 0; top: 0; width: 12px; height: 100px; }
</style>
</head>
<body>

  <section class="sheet sheet--light letterhead" aria-label="Letterhead">
    <div class="brand"><span class="brand__mark"></span>MuroDeck Nordhaven</div>
    <address class="address address--ruled-right">MuroDeck Nordhaven<br>Street Name 35<br>23412 City</address>
    <div class="color-band color-band--vertical" role="img" aria-label="Stepped band of print colour swatches"></div>
  </section>

  <section class="sheet sheet--dark folder" aria-label="Presentation folder">
    <div class="brand"><span class="brand__mark"></span>MuroDeck Nordhaven</div>
    <div class="color-band color-band--folder" role="img" aria-label="Stepped columns of print colour swatches"></div>
  </section>

  <section class="sheet sheet--light envelope-front" aria-label="Envelope front">
    <div class="brand"><span class="brand__mark"></span>MuroDeck Nordhaven</div>
    <address class="address address--ruled-left">MuroDeck Nordhaven<br>Street Name 35<br>23412 City</address>
    <div class="color-band color-band--vertical" role="img" aria-label="Stepped band of print colour swatches"></div>
  </section>

  <section class="sheet sheet--light envelope-back" aria-label="Envelope back">
    <svg class="flap" viewBox="0 0 360 180" preserveAspectRatio="none" aria-hidden="true">
      <path d="M0 0 H360 V40 Q180 88 0 40 Z" fill="#2e2e2e"/>
      <path d="M0 180 L150 95 Q180 82 210 95 L360 180" fill="none" stroke="#e2e2e2" stroke-width="1"/>
    </svg>
    <div class="web">www.murodeck.example</div>
    <div class="color-band color-band--vertical" role="img" aria-label="Stepped band of print colour swatches"></div>
  </section>

  <section class="sheet sheet--light card card--light" aria-label="Business card front">
    <div class="brand"><span class="brand__mark"></span>MuroDeck Nordhaven</div>
    <address class="address">MuroDeck Nordhaven<br>Street Name 35<br>23412 City</address>
    <div class="person">
      <div class="person__name">Erik Lundvall</div>
      <div class="person__role">Director</div>
    </div>
  </section>

  <section class="sheet sheet--dark card card--dark" aria-label="Business card back">
    <div class="brand"><span class="brand__mark"></span>MuroDeck Nordhaven</div>
    <div class="color-band color-band--vertical" role="img" aria-label="Stepped band of print colour swatches"></div>
  </section>

</body>
</html>
```